WordPress Website Design - Brennick Auction

Need a WordPress design for an auction company wanting a responsive, simple and easy to use site. Current site to be upgraded: http://www.brennickauctions.example/

A site the client mentions liking is http://www.taverlyauction.example. The attached logo color can be changed to suit your design - a different red, or green perhaps.

Industry/Entity Type

It Company

Number of Pages Required

1 page

Font styles to use
Serif
Sans Serif

Requirements
Must have
• Keep in mind this site will be built on a responsive theme.
• Site navigation: 1) Home, 2) Auctions, 3) Real Estate Listings, 4) Services, 5) Appraisals, 6) The Gavel Hall, 7) About Us, 8) Contact Us
• Site will have large, prominent full width (960px) slideshow - please pick one of the 3 attached images. Colors can be different than current site - wants a brighter site, colors complementing the logo. Home page will have auction list (the look of the auction list can be seen at http://www.northgateholdingsweb.example/auction-calendar/)
• The widgets in the sidebar/header are: Email signup form, social media(FB Twitter, Youtube), News & Events blog, Testimonials, Featured Auctions, Featured Listings widget.
• Footer will have smaller company logo(below), contact info, and attached association logos.
• Gordon Brennick Auction-Realty
• 3817 Pelham Court • Castor Falls, IN 47088
• dominic@brennickauctions.example
• 812.555.0146
• 877.555.0193
Nice to have
• Design of dropdown menus: under Auctions, 1) Current Auctions, 2) Online Auctions, 3) Past Auctions

```html
<!DOCTYPE html>
<html lang="en">
<head>
<meta charset="utf-8">
<title>Brennick Auction — Home</title>
<link href="https://fonts.googleapis.com/css2?family=Open+Sans:wght@400;600;700&family=Raleway:wght@600;700;800&display=swap" rel="stylesheet">
<style>
:root{
  --red:#e23b4f;
  --red-dark:#c42e41;
  --nav:#474747;
  --bar:#555555;
  --ink:#333333;
  --muted:#777777;
  --page:#ececec;
  --white:#ffffff;
  --footer:#262626;
  --black:#1c1c1c;
}
*{box-sizing:border-box;margin:0;padding:0}
html,body{width:1200px;height:3116px;overflow:hidden}
body{font-family:"Open Sans",Arial,sans-serif;color:var(--ink);background:var(--white);font-size:13px;line-height:1.45}
a{color:inherit;text-decoration:none}

/* Header */
.site-header{height:72px;display:flex;align-items:center;justify-content:space-between;padding:0 40px}
.brand{display:flex;align-items:center;gap:10px;font-family:"Raleway",sans-serif;font-weight:800;font-size:30px;color:var(--red);letter-spacing:-.3px}
.brand-dot{width:12px;height:12px;border-radius:50%;background:var(--red)}
.header-icons{display:flex;gap:10px}
.header-icons span{width:26px;height:26px;border-radius:50%;border:2px solid #cfcfcf}

/* Navigation */
.main-nav{height:40px;background:var(--nav);padding:0 40px;display:flex}
.main-nav a{display:flex;align-items:center;padding:0 24px;color:#eee;font-size:13px;font-weight:600}
.main-nav a.active{background:var(--red);color:var(--white)}

/* Hero */
.hero{position:relative;height:548px;overflow:hidden}
.hero-photo{position:absolute;inset:0;background:linear-gradient(180deg,#b9c3cd 0%,#cdd2d2 22%,#a99a86 40%,#8e7d64 62%,#7d8a5e 82%,#6f7c55 100%)}
.hero-panel{position:absolute;right:20px;top:170px;width:560px;height:260px;background:rgba(226,59,79,.92);clip-path:polygon(9% 0,100% 0,100% 100%,0 100%);padding:34px 40px 0 90px;color:var(--white);text-align:right}
.hero-panel h1{font-family:"Raleway",sans-serif;font-weight:700;font-size:36px;line-height:1.12;letter-spacing:.5px}
.hero-panel p{font-size:13px;margin-top:12px}
.btn-light{display:inline-block;margin-top:18px;background:var(--white);color:var(--ink);font-size:11px;font-weight:700;padding:9px 20px;letter-spacing:.5px}
.hero-arrows{position:absolute;left:50%;bottom:28px;transform:translateX(-50%);display:flex;gap:14px}
.hero-arrows svg{width:16px;height:16px}

/* Content */
.content{background:var(--page);height:2080px;padding:60px 48px 0 40px;position:relative}
.section-title{font-family:"Raleway",sans-serif;font-weight:700;font-size:22px;color:var(--red);text-transform:uppercase;letter-spacing:.5px}
.columns{display:flex;justify-content:space-between;margin-top:26px}
.auction-list{width:720px;display:flex;flex-direction:column;gap:24px}
.auction-card{height:288px;background:var(--white)}
.auction-card-bar{height:40px;background:var(--bar);color:var(--white);font-size:13px;font-weight:700;text-transform:uppercase;display:flex;align-items:center;padding:0 20px;letter-spacing:.3px}
.auction-card-body{display:flex;gap:26px;padding:20px}
.auction-media{width:300px}
.auction-photo{height:160px}
.auction-buttons{display:flex;gap:14px;margin-top:36px}
.btn{display:flex;align-items:center;justify-content:center;gap:8px;width:118px;height:32px;color:var(--white);font-size:11px;font-weight:700;letter-spacing:.5px}
.btn svg{width:12px;height:12px}
.btn-red{background:var(--red)}
.btn-black{background:var(--black)}
.auction-info h3{font-family:"Raleway",sans-serif;color:var(--red);font-size:19px;font-weight:700}
.auction-info p{font-size:12px;color:var(--muted);margin-top:6px;max-width:330px}
.meta{display:flex;gap:8px;margin-top:12px;font-size:12px;color:var(--ink)}
.meta svg{width:14px;height:14px;flex:none;margin-top:2px}
.meta b{width:70px;flex:none}

/* Sidebar */
.sidebar{width:344px;display:flex;flex-direction:column;gap:28px}
.widget{background:var(--white)}
.widget-title{height:40px;background:var(--red);color:var(--white);font-family:"Raleway",sans-serif;font-weight:700;font-size:15px;display:flex;align-items:center;padding:0 16px}
.widget-body{padding:18px 16px}
.field{height:34px;border:1px solid #d5d5d5;font-size:12px;color:#999;display:flex;align-items:center;padding:0 10px}
.btn-grey{margin:14px auto 0;width:140px;height:32px;background:#8a8a8a;color:var(--white);font-size:11px;font-weight:700;display:flex;align-items:center;justify-content:center}
.social{display:flex;justify-content:center;gap:22px;padding:26px 0}
.social span{width:42px;height:42px;background:var(--red)}
.view-all{display:block;text-align:right;font-size:10px;font-weight:700;color:var(--red);margin-top:8px;text-transform:uppercase}
.news-item{display:flex;gap:12px;padding:8px 0;border-bottom:1px solid #eee}
.date-box{width:52px;height:52px;background:var(--red);color:var(--white);font-size:11px;font-weight:700;display:flex;flex-direction:column;align-items:center;justify-content:center;line-height:1.2;flex:none}
.date-box strong{font-size:17px}
.item-text h4{font-size:12px;font-weight:700}
.item-text p{font-size:11px;color:var(--muted)}
.person{display:flex;gap:14px;padding:10px 0;border-bottom:1px solid #eee}
.avatar-round{width:58px;height:58px;border-radius:50%;background:#c7b8a8;flex:none}
.avatar-square{width:48px;height:48px;background:#bfb7ae;flex:none}
.read-more{font-size:10px;color:var(--red);font-weight:700;display:block;text-align:right}
.thumbs{display:flex;gap:14px}
.thumbs div{flex:1;height:120px}

/* Footer */
.footer-brand{height:240px;display:flex;flex-direction:column;align-items:center;justify-content:center;gap:34px}
.footer-brand .brand{font-size:28px}
.partners{display:flex;gap:36px}
.partners span{width:150px;height:64px;border:2px solid #d8d8d8;background:#f6f6f6}
.site-footer{height:136px;background:var(--footer);color:#ddd;display:flex;flex-direction:column;justify-content:center;gap:16px;padding:0 140px}
.contact-row{display:flex;justify-content:space-between;font-size:17px;font-weight:600}
.contact{display:flex;align-items:center;gap:12px}
.icon-circle{width:30px;height:30px;border-radius:50%;background:var(--red);display:flex;align-items:center;justify-content:center}
.icon-circle svg{width:15px;height:15px}
.address{display:flex;align-items:center;gap:12px;font-size:13px}
</style>
</head>
<body>

<header class="site-header">
  <a class="brand" href="#"><span>Brennick Auction</span><span class="brand-dot"></span></a>
  <div class="header-icons"><span></span><span></span></div>
</header>

<nav class="main-nav">
  <a class="active" href="#">Home</a>
  <a href="#">Auctions</a>
  <a href="#">Real Estate Listings</a>
  <a href="#">Services</a>
  <a href="#">Appraisals</a>
  <a href="#">The Gavel Hall</a>
  <a href="#">About Us</a>
  <a href="#">Contact Us</a>
</nav>

<section class="hero">
  <div class="hero-photo" role="img" aria-label="Aerial view of farmland fields and a country road under a pale sky"></div>
  <div class="hero-panel">
    <h1>LOREM IPSUM DOLOR<br>SIT AMET LOROLSD</h1>
    <p>Lorem ipsum dolor sit amet, consectetur adipiscing elit, sed do eiusmod tempor incididunt ut labore et dolore magna aliqua. Ut enim ad minim veniam.</p>
    <a class="btn-light" href="#">READ MORE</a>
  </div>
  <div class="hero-arrows">
    <svg viewBox="0 0 16 16"><path d="M11 2 5 8l6 6" fill="none" stroke="#fff" stroke-width="2.5"/></svg>
    <svg viewBox="0 0 16 16"><path d="m5 2 6 6-6 6" fill="none" stroke="#fff" stroke-width="2.5"/></svg>
  </div>
</section>

<main class="content">
  <h2 class="section-title">Featured Auctions</h2>
  <div class="columns">

    <div class="auction-list">
      <article class="auction-card">
        <div class="auction-card-bar">Sealed Bid Real Estate Auction</div>
        <div class="auction-card-body">
          <div class="auction-media">
            <div class="auction-photo" role="img" aria-label="Single-storey home with grey siding and a front porch" style="background:linear-gradient(180deg,#a9c3dc,#c9c7bf 55%,#7f9467)"></div>
            <div class="auction-buttons">
              <a class="btn btn-red" href="#"><svg viewBox="0 0 12 12"><rect x="1" y="1" width="10" height="10" fill="none" stroke="#fff" stroke-width="1.5"/></svg>DETAILS</a>
              <a class="btn btn-black" href="#"><svg viewBox="0 0 12 12"><rect x="1" y="3" width="10" height="7" fill="#fff"/></svg>PHOTOS</a>
            </div>
          </div>
          <div class="auction-info">
            <h3>Sealed Bid Auction</h3>
            <p>Lorem ipsum dolor sit amet, consectetur adipiscing elit, sed do eiusmod tempor incididunt.</p>
            <div class="meta"><svg viewBox="0 0 14 14"><circle cx="7" cy="7" r="6" fill="none" stroke="#e23b4f" stroke-width="1.6"/><path d="M7 3.5V7h3" fill="none" stroke="#e23b4f" stroke-width="1.6"/></svg><b>Begins:</b><span>Wednesday, August 12, 2015<br>at 5:00 PM EST</span></div>
            <div class="meta"><svg viewBox="0 0 14 14"><path d="M7 13S2.5 8 2.5 5.2a4.5 4.5 0 0 1 9 0C11.5 8 7 13 7 13z" fill="#e23b4f"/><circle cx="7" cy="5.2" r="1.6" fill="#fff"/></svg><b>Location:</b><span>Gordon Brennick Auction-Realty<br>3817 Pelham Court, Castor Falls, IN 47088</span></div>
          </div>
        </div>
      </article>

      <article class="auction-card">
        <div class="auction-card-bar">Sealed Bid Real Estate Auction</div>
        <div class="auction-card-body">
          <div class="auction-media">
            <div class="auction-photo" role="img" aria-label="Two-storey brick house with a wide front lawn" style="background:linear-gradient(180deg,#9fbfe0,#a58f7a 55%,#6e8a4f)"></div>
            <div class="auction-buttons">
              <a class="btn btn-red" href="#"><svg viewBox="0 0 12 12"><rect x="1" y="1" width="10" height="10" fill="none" stroke="#fff" stroke-width="1.5"/></svg>DETAILS</a>
              <a class="btn btn-black" href="#"><svg viewBox="0 0 12 12"><rect x="1" y="3" width="10" height="7" fill="#fff"/></svg>PHOTOS</a>
            </div>
          </div>
          <div class="auction-info">
            <h3>Sealed Bid Auction</h3>
            <p>Lorem ipsum dolor sit amet, consectetur adipiscing elit, sed do eiusmod tempor incididunt.</p>
            <div class="meta"><svg viewBox="0 0 14 14"><circle cx="7" cy="7" r="6" fill="none" stroke="#e23b4f" stroke-width="1.6"/><path d="M7 3.5V7h3" fill="none" stroke="#e23b4f" stroke-width="1.6"/></svg><b>Begins:</b><span>Wednesday, August 12, 2015<br>at 5:00 PM EST</span></div>
            <div class="meta"><svg viewBox="0 0 14 14"><path d="M7 13S2.5 8 2.5 5.2a4.5 4.5 0 0 1 9 0C11.5 8 7 13 7 13z" fill="#e23b4f"/><circle cx="7" cy="5.2" r="1.6" fill="#fff"/></svg><b>Location:</b><span>Gordon Brennick Auction-Realty<br>3817 Pelham Court, Castor Falls, IN 47088</span></div>
          </div>
        </div>
      </article>

      <article class="auction-card">
        <div class="auction-card-bar">Sealed Bid Real Estate Auction</div>
        <div class="auction-card-body">
          <div class="auction-media">
            <div class="auction-photo" role="img" aria-label="White two-storey house with blue shutters" style="background:linear-gradient(180deg,#8fb4de,#dfe2e4 50%,#7c9a5a)"></div>
            <div class="auction-buttons">
              <a class="btn btn-red" href="#"><svg viewBox="0 0 12 12"><rect x="1" y="1" width="10" height="10" fill="none" stroke="#fff" stroke-width="1.5"/></svg>DETAILS</a>
              <a class="btn btn-black" href="#"><svg viewBox="0 0 12 12"><rect x="1" y="3" width="10" height="7" fill="#fff"/></svg>PHOTOS</a>
            </div>
          </div>
          <div class="auction-info">
            <h3>Sealed Bid Auction</h3>
            <p>Lorem ipsum dolor sit amet, consectetur adipiscing elit, sed do eiusmod tempor incididunt.</p>
            <div class="meta"><svg viewBox="0 0 14 14"><circle cx="7" cy="7" r="6" fill="none" stroke="#e23b4f" stroke-width="1.6"/><path d="M7 3.5V7h3" fill="none" stroke="#e23b4f" stroke-width="1.6"/></svg><b>Begins:</b><span>Wednesday, August 12, 2015<br>at 5:00 PM EST</span></div>
            <div class="meta"><svg viewBox="0 0 14 14"><path d="M7 13S2.5 8 2.5 5.2a4.5 4.5 0 0 1 9 0C11.5 8 7 13 7 13z" fill="#e23b4f"/><circle cx="7" cy="5.2" r="1.6" fill="#fff"/></svg><b>Location:</b><span>Gordon Brennick Auction-Realty<br>3817 Pelham Court, Castor Falls, IN 47088</span></div>
          </div>
        </div>
      </article>

      <article class="auction-card">
        <div class="auction-card-bar">Sealed Bid Real Estate Auction</div>
        <div class="auction-card-body">
          <div class="auction-media">
            <div class="auction-photo" role="img" aria-label="Beige family house with a double garage" style="background:linear-gradient(180deg,#a7c6e3,#c6b59c 55%,#7a9257)"></div>
            <div class="auction-buttons">
              <a class="btn btn-red" href="#"><svg viewBox="0 0 12 12"><rect x="1" y="1" width="10" height="10" fill="none" stroke="#fff" stroke-width="1.5"/></svg>DETAILS</a>
              <a class="btn btn-black" href="#"><svg viewBox="0 0 12 12"><rect x="1" y="3" width="10" height="7" fill="#fff"/></svg>PHOTOS</a>
            </div>
          </div>
          <div class="auction-info">
            <h3>Sealed Bid Auction</h3>
            <p>Lorem ipsum dolor sit amet, consectetur adipiscing elit, sed do eiusmod tempor incididunt.</p>
            <div class="meta"><svg viewBox="0 0 14 14"><circle cx="7" cy="7" r="6" fill="none" stroke="#e23b4f" stroke-width="1.6"/><path d="M7 3.5V7h3" fill="none" stroke="#e23b4f" stroke-width="1.6"/></svg><b>Begins:</b><span>Wednesday, August 12, 2015<br>at 5:00 PM EST</span></div>
            <div class="meta"><svg viewBox="0 0 14 14"><path d="M7 13S2.5 8 2.5 5.2a4.5 4.5 0 0 1 9 0C11.5 8 7 13 7 13z" fill="#e23b4f"/><circle cx="7" cy="5.2" r="1.6" fill="#fff"/></svg><b>Location:</b><span>Gordon Brennick Auction-Realty<br>3817 Pelham Court, Castor Falls, IN 47088</span></div>
          </div>
        </div>
      </article>

      <article class="auction-card">
        <div class="auction-card-bar">Sealed Bid Real Estate Auction</div>
        <div class="auction-card-body">
          <div class="auction-media">
            <div class="auction-photo" role="img" aria-label="Large stone house surrounded by green trees" style="background:linear-gradient(180deg,#9cc0e2,#9c9282 50%,#5f8045)"></div>
            <div class="auction-buttons">
              <a class="btn btn-red" href="#"><svg viewBox="0 0 12 12"><rect x="1" y="1" width="10" height="10" fill="none" stroke="#fff" stroke-width="1.5"/></svg>DETAILS</a>
              <a class="btn btn-black" href="#"><svg viewBox="0 0 12 12"><rect x="1" y="3" width="10" height="7" fill="#fff"/></svg>PHOTOS</a>
            </div>
          </div>
          <div class="auction-info">
            <h3>Sealed Bid Auction</h3>
            <p>Lorem ipsum dolor sit amet, consectetur adipiscing elit, sed do eiusmod tempor incididunt.</p>
            <div class="meta"><svg viewBox="0 0 14 14"><circle cx="7" cy="7" r="6" fill="none" stroke="#e23b4f" stroke-width="1.6"/><path d="M7 3.5V7h3" fill="none" stroke="#e23b4f" stroke-width="1.6"/></svg><b>Begins:</b><span>Wednesday, August 12, 2015<br>at 5:00 PM EST</span></div>
            <div class="meta"><svg viewBox="0 0 14 14"><path d="M7 13S2.5 8 2.5 5.2a4.5 4.5 0 0 1 9 0C11.5 8 7 13 7 13z" fill="#e23b4f"/><circle cx="7" cy="5.2" r="1.6" fill="#fff"/></svg><b>Location:</b><span>Gordon Brennick Auction-Realty<br>3817 Pelham Court, Castor Falls, IN 47088</span></div>
          </div>
        </div>
      </article>

      <article class="auction-card">
        <div class="auction-card-bar">Sealed Bid Real Estate Auction</div>
        <div class="auction-card-body">
          <div class="auction-media">
            <div class="auction-photo" role="img" aria-label="White colonial house with a tidy green yard" style="background:linear-gradient(180deg,#b0cbe6,#e4e2dc 50%,#6f9150)"></div>
            <div class="auction-buttons">
              <a class="btn btn-red" href="#"><svg viewBox="0 0 12 12"><rect x="1" y="1" width="10" height="10" fill="none" stroke="#fff" stroke-width="1.5"/></svg>DETAILS</a>
              <a class="btn btn-black" href="#"><svg viewBox="0 0 12 12"><rect x="1" y="3" width="10" height="7" fill="#fff"/></svg>PHOTOS</a>
            </div>
          </div>
          <div class="auction-info">
            <h3>Sealed Bid Auction</h3>
            <p>Lorem ipsum dolor sit amet, consectetur adipiscing elit, sed do eiusmod tempor incididunt.</p>
            <div class="meta"><svg viewBox="0 0 14 14"><circle cx="7" cy="7" r="6" fill="none" stroke="#e23b4f" stroke-width="1.6"/><path d="M7 3.5V7h3" fill="none" stroke="#e23b4f" stroke-width="1.6"/></svg><b>Begins:</b><span>Wednesday, August 12, 2015<br>at 5:00 PM EST</span></div>
            <div class="meta"><svg viewBox="0 0 14 14"><path d="M7 13S2.5 8 2.5 5.2a4.5 4.5 0 0 1 9 0C11.5 8 7 13 7 13z" fill="#e23b4f"/><circle cx="7" cy="5.2" r="1.6" fill="#fff"/></svg><b>Location:</b><span>Gordon Brennick Auction-Realty<br>3817 Pelham Court, Castor Falls, IN 47088</span></div>
          </div>
        </div>
      </article>
    </div>

    <aside class="sidebar">
      <section class="widget" style="height:200px">
        <h3 class="widget-title">Newsletter Sign Up</h3>
        <div class="widget-body">
          <div class="field">Your name</div>
          <div class="field" style="margin-top:10px">Your email address</div>
          <a class="btn-grey" href="#">SUBSCRIBE</a>
        </div>
      </section>

      <section class="widget" style="height:130px">
        <h3 class="widget-title">Social Media</h3>
        <div class="social"><span></span><span></span><span></span></div>
      </section>

      <section class="widget" style="height:250px">
        <h3 class="widget-title">News</h3>
        <div class="widget-body">
          <div class="news-item"><div class="date-box"><strong>19</strong>Aug</div><div class="item-text"><h4>Lorem ipsum dolor sit amet</h4><p>Consectetur adipiscing elit, sed do eiusmod tempor.</p></div></div>
          <div class="news-item"><div class="date-box"><strong>19</strong>Aug</div><div class="item-text"><h4>Lorem ipsum dolor sit amet</h4><p>Consectetur adipiscing elit, sed do eiusmod tempor.</p></div></div>
          <a class="view-all" href="#">View all</a>
        </div>
      </section>

      <section class="widget" style="height:300px">
        <h3 class="widget-title">Events Blog</h3>
        <div class="widget-body">
          <div class="person"><div class="avatar-round" role="img" aria-label="Event author portrait"></div><div class="item-text"><h4>Lorem ipsum dolor sit amet</h4><p>Consectetur adipiscing elit, sed do eiusmod tempor incididunt ut labore.</p></div></div>
          <div class="person"><div class="avatar-round" role="img" aria-label="Event author portrait" style="background:#d2b49c"></div><div class="item-text"><h4>Lorem ipsum dolor sit amet</h4><p>Consectetur adipiscing elit, sed do eiusmod tempor incididunt ut labore.</p></div></div>
          <a class="view-all" href="#">View all</a>
        </div>
      </section>

      <section class="widget" style="height:290px">
        <h3 class="widget-title">Testimonials</h3>
        <div class="widget-body">
          <div class="person"><div class="avatar-square" role="img" aria-label="Client portrait"></div><div class="item-text"><p>Lorem ipsum dolor sit amet, consectetur adipiscing elit, sed do eiusmod tempor incididunt.</p><a class="read-more" href="#">read more</a></div></div>
          <div class="person"><div class="avatar-square" role="img" aria-label="Client portrait"></div><div class="item-text"><p>Lorem ipsum dolor sit amet, consectetur adipiscing elit, sed do eiusmod tempor incididunt.</p><a class="read-more" href="#">read more</a></div></div>
        </div>
      </section>

      <section class="widget" style="height:220px">
        <h3 class="widget-title">Featured Auctions</h3>
        <div class="widget-body">
          <div class="thumbs">
            <div role="img" aria-label="Featured auction house" style="background:linear-gradient(180deg,#a9c6e3,#d8d3c8 55%,#7b9659)"></div>
            <div role="img" aria-label="Featured auction house" style="background:linear-gradient(180deg,#b3cde6,#cfcac0 55%,#84a062)"></div>
          </div>
          <a class="view-all" href="#">View all</a>
        </div>
      </section>

      <section class="widget" style="height:240px">
        <h3 class="widget-title">Featured Listings</h3>
        <div class="widget-body">
          <div class="thumbs">
            <div role="img" aria-label="Featured listing home" style="background:linear-gradient(180deg,#9fc0e0,#c2b29a 55%,#6f8e4f)"></div>
            <div role="img" aria-label="Featured listing home with pool" style="background:linear-gradient(180deg,#a8c9e6,#dcd8cf 50%,#5fa3c9)"></div>
          </div>
          <a class="view-all" href="#">View all</a>
        </div>
      </section>
    </aside>
  </div>
</main>

<section class="footer-brand">
  <a class="brand" href="#"><span>Brennick Auction</span><span class="brand-dot"></span></a>
  <div class="partners"><span></span><span></span><span></span><span></span></div>
</section>

<footer class="site-footer">
  <div class="contact-row">
    <div class="contact"><span class="icon-circle"><svg viewBox="0 0 16 16"><path d="M4 1.5 6 5 4.6 6.6a8 8 0 0 0 4.8 4.8L11 10l3.5 2-1 2.5C7 14.5 1.5 9 1.5 2.5z" fill="#fff"/></svg></span>812.555.0146</div>
    <div class="contact"><span class="icon-circle"><svg viewBox="0 0 16 16"><path d="M4 1.5 6 5 4.6 6.6a8 8 0 0 0 4.8 4.8L11 10l3.5 2-1 2.5C7 14.5 1.5 9 1.5 2.5z" fill="#fff"/></svg></span>877.555.0193</div>
    <div class="contact"><span class="icon-circle"><svg viewBox="0 0 16 16"><rect x="1.5" y="3.5" width="13" height="9" fill="none" stroke="#fff" stroke-width="1.5"/><path d="m2 4 6 5 6-5" fill="none" stroke="#fff" stroke-width="1.5"/></svg></span>dominic@brennickauctions.example</div>
  </div>
  <div class="address"><span class="icon-circle"><svg viewBox="0 0 16 16"><path d="M8 15S3 9.5 3 6a5 5 0 0 1 10 0c0 3.5-5 9-5 9z" fill="#fff"/><circle cx="8" cy="6" r="1.8" fill="#e23b4f"/></svg></span>Gordon Brennick Auction-Realty, 3817 Pelham Court, Castor Falls, IN 47088</div>
</footer>

</body>
</html>
```